Get me out of Jail business cards!!!!

I need business cards done for my business. I own a BailBonds and I get people out of jail!

Colors are red white and black

I need it to say on the card these details:

Rollin’ Free Bailbonds

452 S Kettering Ave
Arcadia, FL 34266

863-555-0172

Open 24/7

On the back of the card:

Must check in every Tuesday.

______/______/______ court date
____________________ time
You must know your court date at all times!

Marla Tisdell - owner
Rosalind Tisdell - agent
Denise Crandon - agent

Industry/Entity Type

Bail bonds

Contact Information for Business Card

Colors are red white and black I need it to say on the card these details: Rollin’ Free Bailbonds 452 S Kettering Ave Arcadia, FL 34266 863-555-0172 Open 24/7 On the back of the card: Must check in every Tuesday. ______/______/______ court date ____________________ time You must know your court date at all times! Marla Tisdell - owner Rosalind Tisdell - agent Denise Crandon - agent

Font styles to use
Serif
Sans Serif

Colors
EB3D1F
EC4F4E
F09395
F8D3D4
FCEDEE

Requirements
Must have
• I listed the must haves in the business card details
Nice to have
• Handcuffs or jail bars or a man in a black and white suit

```html
<!DOCTYPE html>
<html lang="en">
<head>
<meta charset="utf-8">
<title>Rollin’ Free Bailbonds – Business Card</title>
<link href="https://fonts.googleapis.com/css2?family=Cormorant+SC:wght@500;600;700&family=Poppins:ital,wght@0,400;0,500;1,500&display=swap" rel="stylesheet">
<style>
  :root {
    --backdrop: #7b7b7b;
    --ink-black: #000000;
    --ink-white: #ffffff;
    --brand-red: #e30a13;
    --text-gray: #3d3d3d;
    --text-dark: #161616;
    --photo-dark: #2a2a2a;
    --photo-mid: #8e8e8e;
    --corridor-light: #eef2f4;
    --corridor-mid: #d5dde1;
  }
  * { margin: 0; padding: 0; box-sizing: border-box; }
  html, body {
    width: 1093px; height: 1200px; overflow: hidden;
    background: var(--backdrop);
  }
  .canvas { position: relative; width: 1093px; height: 1200px; }

  .card {
    position: absolute; left: 265px; width: 579px; height: 358px;
    border-radius: 20px; overflow: hidden;
  }

  /* Front */
  .card--front { top: 226px; background: var(--ink-black); color: var(--ink-white); }
  .front__photo {
    position: absolute; top: 0; right: 0; width: 262px; height: 100%;
    background: linear-gradient(135deg, var(--photo-dark) 0%, var(--photo-mid) 55%, #d9d9d9 80%, var(--photo-dark) 100%);
  }
  .brand {
    position: absolute; left: 36px; top: 40px; width: 270px;
    font-family: "Poppins", sans-serif; font-weight: 400;
    font-size: 30px; line-height: 1.12; color: var(--ink-white);
    display: flex; align-items: center; gap: 12px;
  }
  .brand__mark {
    flex: none; width: 14px; height: 14px; border-radius: 50%;
    background: var(--brand-red);
  }
  .address {
    position: absolute; left: 36px; top: 170px;
    font-family: "Cormorant SC", serif; font-weight: 600;
    font-size: 20px; line-height: 1.05; letter-spacing: 0.3px;
  }
  .phone {
    position: absolute; left: 36px; top: 254px;
    font-family: "Cormorant SC", serif; font-weight: 700;
    font-size: 30px; letter-spacing: 0.3px;
  }
  .hours {
    position: absolute; left: 35px; top: 299px;
    font-family: "Cormorant SC", serif; font-weight: 700;
    font-size: 24px; letter-spacing: 0.4px;
  }
  .hours__accent { color: var(--brand-red); }

  /* Back */
  .card--back { top: 621px; background: var(--ink-black); }
  .back__scene {
    position: absolute; left: 0; top: 0; width: 100%; height: 236px;
    background: linear-gradient(90deg, var(--corridor-mid) 0%, var(--corridor-light) 30%, #f7f9fa 50%, var(--corridor-light) 70%, var(--corridor-mid) 100%);
  }
  .checkin {
    position: absolute; left: 0; right: 0; top: 37px; text-align: center;
    font-family: "Poppins", sans-serif; font-weight: 500;
    font-size: 20px; color: var(--text-dark);
  }
  .field {
    position: absolute; font-family: "Poppins", sans-serif; font-weight: 400;
    font-size: 17px; color: var(--text-gray); white-space: nowrap; letter-spacing: 0.5px;
  }
  .field--date { left: 105px; top: 93px; }
  .field--time { left: 151px; top: 135px; }
  .warning {
    position: absolute; left: 0; right: 0; top: 172px; text-align: center;
    font-family: "Poppins", sans-serif; font-weight: 500; font-style: italic;
    font-size: 17px; color: var(--brand-red);
  }
  .back__mark {
    position: absolute; left: 271px; top: 221px; width: 36px; height: 36px;
    border-radius: 50%; background: var(--brand-red);
  }
  .team {
    position: absolute; top: 281px; left: 0; width: 100%;
    font-family: "Poppins", sans-serif; font-weight: 500;
    font-size: 17px; line-height: 1.2; text-align: center;
  }
  .team__member { position: absolute; width: 200px; }
  .team__member:nth-child(1) { left: 13px; }
  .team__member:nth-child(2) { left: 208px; }
  .team__member:nth-child(3) { left: 387px; }
  .team__name { color: var(--ink-white); }
  .team__role { color: var(--brand-red); }
</style>
</head>
<body>
<main class="canvas">

  <section class="card card--front" aria-label="Card front">
    <div class="brand"><span class="brand__mark"></span><span>Rollin’ Free Bailbonds</span></div>
    <p class="address">452 S Kettering Ave<br>Arcadia, FL 34266</p>
    <p class="phone">863-555-0172</p>
    <p class="hours">Open <span class="hours__accent">24/7</span></p>
    <div class="front__photo" role="img" aria-label="Black and white photo of handcuffed hands reaching through jail cell bars"></div>
  </section>

  <section class="card card--back" aria-label="Card back">
    <div class="back__scene" role="img" aria-label="Faded light photo of a jail cell corridor with rows of bars"></div>
    <h2 class="checkin">Must check in every Tuesday</h2>
    <p class="field field--date">Court Date: _ _ _ _ _ _/_ _ _ _ _ _/_ _ _ _ _ _</p>
    <p class="field field--time">Time: _ _ _ _ _ _ _ _ _ _ _ _ _ _ _ _ _ _ _ _ _ _</p>
    <p class="warning">You must know your court date at all times!</p>
    <div class="back__mark"></div>
    <div class="team">
      <div class="team__member"><div class="team__name">Marla Tisdell</div><div class="team__role">Owner</div></div>
      <div class="team__member"><div class="team__name">Rosalind Tisdell</div><div class="team__role">Agent</div></div>
      <div class="team__member"><div class="team__name">Denise Crandon</div><div class="team__role">Agent</div></div>
    </div>
  </section>

</main>
</body>
</html>
```